New Template, new corporate image Quelmoro 2022

New template designs for google slides or PowerPoint. Match to new corporate image. The new website www.quelmoro-mx.com Needs to match our new version. Technology and Artificial Intelligence elements to reflect our type of work.
We are adding old version of template and will send elements for the new corporate images.
Please consider our website as the main corporate image.
Our templates are being used on customer presentations, webminars, internal work only.
We have our main name of company Quelmoro. Quelmoro has to be in all the templates.
Secondary logo or branded service is: Calvindar.

Target Market(s)

Industrial users. Asset managers. Corporate visitors and customers.

Industry/Entity Type

Automotive. Chemical. Food and Beverage. Manufacturing

Other font styles liked:
• GE INSPIRA. RALEWAY

Colors
0054AA
0677BA
7BADD7
CADEEF
E8F1F8

Requirements
Must have
• Match to our elements on the new image. Use Brain Icons. Chips icons to connect equipments with software and control. Innovation.
Nice to have
• Unique images, machine images. Connecting machines and data elements. Template version for google slides. Image for industrial software for control equipment and saving money to manufacturers. Segments: Automotive, Chemical, Food and Beverages, Mining and pharmaceutical, Energy Management
Should not have
• old elements. not to much images of medical devices. Do not seems like a hospital.

```html
<!DOCTYPE html>
<html lang="en">
<head>
<meta charset="utf-8">
<title>Quelmoro – Industrial Data Hub slides</title>
<link rel="stylesheet" href="https://fonts.googleapis.com/css2?family=Raleway:wght@400;500;600;700;800&family=Titillium+Web:wght@200;300&display=swap">
<style>
:root{
  --navy:#0b2f6b;
  --brand:#0054AA;
  --mid:#0677BA;
  --sky:#7BADD7;
  --pale:#CADEEF;
  --mist:#E8F1F8;
  --agenda-bg:#E2ECF6;
  --contact-bg:#C3D8EC;
  --ink:#1d2430;
  --title-blue:#0b3f93;
}
*{margin:0;padding:0;box-sizing:border-box}
html,body{width:1200px;height:3654px;overflow:hidden;background:#fff}
body{position:relative;font-family:"Raleway",sans-serif;color:var(--ink)}
.slide{position:absolute;left:98px;width:985px;height:553px;overflow:hidden}
.slide svg.bg{position:absolute;inset:0;width:985px;height:553px}
.thin{font-family:"Titillium Web",sans-serif;font-weight:300;letter-spacing:1px;text-transform:uppercase}
.abs{position:absolute}

/* cover */
.cover{top:56px;background:var(--brand)}
.cover .brand-word{left:38px;top:58px;font-size:54px;color:#fff}
.cover .headline{left:48px;top:150px;font-size:54px;line-height:52px;font-weight:800;color:#fff}
.cover .lead{left:43px;top:280px;width:380px;font-size:18.5px;line-height:29px;color:#eaf2fb}

/* agenda */
.agenda{top:638px;background:var(--agenda-bg)}
.agenda .label{left:52px;top:210px;font-size:40px;color:#1c1c1c}
.wordmark{font-family:"Raleway",sans-serif;font-weight:700;color:var(--brand);letter-spacing:1px}
.agenda .wordmark{left:18px;top:282px;font-size:30px}
.agenda .item{position:absolute;width:560px}
.agenda .item h3{font-size:16px;font-weight:700;color:var(--title-blue);margin-bottom:5px}
.agenda .item p{font-size:12.5px;line-height:21px;color:#222}
.num{position:absolute;width:44px;height:44px;border-radius:50%;color:#fff;font-weight:700;font-size:18px;display:flex;align-items:center;justify-content:center}

/* apply */
.apply{top:1224px;background:#0a1540}
.apply .title{left:30px;top:64px;font-size:40px;line-height:47px;color:#fff}
.feature{position:absolute;display:flex;align-items:center;gap:16px}
.ring{width:72px;height:72px;border-radius:50%;border:2px solid #fff;flex:none;display:flex;align-items:center;justify-content:center}
.feature p{font-size:12.5px;line-height:21.5px;color:#fff;width:300px}

/* apm */
.apm{top:1810px;background:var(--agenda-bg)}
.apm .title{left:30px;top:68px;font-size:40px;line-height:47px;color:#1c1c1c}
.checks{position:absolute;left:30px;top:228px;list-style:none;width:510px}
.checks li{display:flex;gap:18px;font-size:12.5px;line-height:20px;color:var(--title-blue);font-weight:500;margin-bottom:9px}
.checks svg{flex:none;margin-top:3px}
.apm .note{left:34px;top:390px;width:470px;font-size:11.5px;line-height:18px;color:#222}

/* hyper */
.hyper{top:2395px;background:#0c5fb3}
.hyper .title{left:492px;top:95px;font-size:40px;line-height:47px;color:#fff}
.hyper .para{position:absolute;width:470px;font-size:11.5px;line-height:18px;color:#eaf2fb}

/* contacts */
.contacts{top:2986px;background:var(--contact-bg)}
.contacts .title{left:45px;top:128px;font-size:46px;color:#1c1c1c}
.contacts .wordmark{left:48px;top:196px;font-size:24px}
.contact-row{position:absolute;left:46px;display:flex;align-items:center;gap:20px;font-size:17px;line-height:25px;color:#1c1c1c;font-family:"Titillium Web",sans-serif;font-weight:300}
.dot{width:44px;height:44px;border-radius:50%;background:var(--mid);flex:none;display:flex;align-items:center;justify-content:center}
</style>
</head>
<body>

<!-- Cover -->
<section class="slide cover">
  <svg class="bg" viewBox="0 0 985 553">
    <defs>
      <radialGradient id="brainGlow" cx="0.65" cy="0.35" r="0.6">
        <stop offset="0" stop-color="#1e7fd6"/>
        <stop offset="0.45" stop-color="#0b2a55"/>
        <stop offset="1" stop-color="#050c1c"/>
      </radialGradient>
    </defs>
    <polygon points="678,0 985,0 985,553 269,553" fill="url(#brainGlow)" role="img" aria-label="Glowing digital brain rising from a circuit chip"/>
    <polygon points="985,360 985,553 850,553" fill="var(--sky)"/>
  </svg>
  <div class="abs thin brand-word">Quelmoro</div>
  <h1 class="abs headline">Industrial<br>Data Hub</h1>
  <p class="abs lead">Sed ut perspiciatis unde omnis iste natus error sit voluptatem accusantium doloremque quasi architecto beatae vitae dicta sunt explicabo.</p>
</section>

<!-- Agenda -->
<section class="slide agenda">
  <svg class="bg" viewBox="0 0 985 553">
    <circle cx="10" cy="273" r="262" fill="none" stroke="#fff" stroke-width="14"/>
    <polygon points="846,0 985,0 985,198" fill="var(--sky)"/>
    <polygon points="550,553 611,467 672,553" fill="var(--sky)"/>
  </svg>
  <div class="abs thin label">Agenda</div>
  <div class="abs wordmark">Quelmoro</div>

  <div class="num" style="left:196px;top:115px;background:var(--title-blue)">1</div>
  <div class="item" style="left:266px;top:100px"><h3>Sed ut perspiciatis unde omnis iste</h3><p>Natus error sit voluptatem accusantium doloremque laudantium, totam rem aperiam<br>sint occaecat cupidatat non proident.</p></div>

  <div class="num" style="left:236px;top:205px;background:var(--mid)">2</div>
  <div class="item" style="left:298px;top:197px"><h3>Sed ut perspiciatis unde omnis iste</h3><p>Natus error sit voluptatem accusantium doloremque laudantium, totam rem aperiam<br>sint occaecat cupidatat non proident.</p></div>

  <div class="num" style="left:240px;top:303px;background:#444">3</div>
  <div class="item" style="left:314px;top:294px"><h3>Sed ut perspiciatis unde omnis iste</h3><p>Natus error sit voluptatem accusantium doloremque laudantium, totam rem aperiam<br>sint occaecat cupidatat non proident.</p></div>

  <div class="num" style="left:197px;top:401px;background:var(--sky)">4</div>
  <div class="item" style="left:266px;top:391px"><h3>Sed ut perspiciatis unde omnis iste</h3><p>Natus error sit voluptatem accusantium doloremque laudantium, totam rem aperiam<br>sint occaecat cupidatat non proident.</p></div>
</section>

<!-- Where to apply -->
<section class="slide apply">
  <svg class="bg" viewBox="0 0 985 553">
    <defs>
      <radialGradient id="chipGlow" cx="0.45" cy="0.55" r="0.6">
        <stop offset="0" stop-color="#1a3aa8"/>
        <stop offset="0.5" stop-color="#0c1a5c"/>
        <stop offset="1" stop-color="#060b2e"/>
      </radialGradient>
      <linearGradient id="factory" x1="0" y1="0" x2="1" y2="1">
        <stop offset="0" stop-color="#9fb0c8"/>
        <stop offset="1" stop-color="#3c4a66"/>
      </linearGradient>
    </defs>
    <rect width="985" height="553" fill="url(#chipGlow)" role="img" aria-label="Blue circuit board with an AI processor chip"/>
    <polygon points="533,0 985,0 732,311" fill="url(#factory)" role="img" aria-label="Hands holding a tablet with a dashboard in a factory"/>
    <polygon points="45,553 140,394 307,553" fill="var(--sky)"/>
  </svg>
  <h2 class="abs thin title">Where to apply industrial<br>data hub?</h2>

  <div class="feature" style="left:30px;top:196px"><div class="ring"><svg width="34" height="34" viewBox="0 0 34 34" fill="none" stroke="#fff" stroke-width="1.6"><rect x="9" y="9" width="16" height="16"/><path d="M13 9V4M17 9V4M21 9V4M13 30v-5M17 30v-5M21 30v-5M9 13H4M9 17H4M9 21H4M30 13h-5M30 17h-5M30 21h-5"/></svg></div><p>Sed ut perspiciatis unde omnis iste natus error sit voluptatem accusantium doloremque laudantium, totam rem aperiam</p></div>

  <div class="feature" style="left:30px;top:298px"><div class="ring"><svg width="34" height="34" viewBox="0 0 34 34" fill="none" stroke="#fff" stroke-width="1.6"><path d="M4 24c5 0 7-3 11-3h8M4 29h18l8-7"/><path d="M17 6v10M13 10h8M15 16h4"/></svg></div><p>Sed ut perspiciatis unde omnis iste natus error sit voluptatem accusantium doloremque laudantium, totam rem aperiam</p></div>

  <div class="feature" style="left:498px;top:298px"><div class="ring"><svg width="34" height="34" viewBox="0 0 34 34" fill="none" stroke="#fff" stroke-width="1.6"><circle cx="13" cy="20" r="7"/><circle cx="13" cy="20" r="2.5"/><circle cx="24" cy="10" r="5"/><circle cx="24" cy="10" r="1.8"/></svg></div><p>Sed ut perspiciatis unde omnis iste natus error sit voluptatem accusantium doloremque laudantium, totam rem aperiam</p></div>

  <div class="feature" style="left:30px;top:400px"><div class="ring"><svg width="34" height="34" viewBox="0 0 34 34" fill="none" stroke="#fff" stroke-width="1.6"><path d="M17 5c-6 0-11 4-11 10 0 4 2 6 4 8v6h10v-4h4l1-5 3-1-3-6c0-5-3-8-8-8z"/><circle cx="15" cy="15" r="3"/></svg></div><p>Sed ut perspiciatis unde omnis iste natus error sit voluptatem accusantium doloremque laudantium, totam rem aperiam</p></div>

  <div class="feature" style="left:498px;top:400px"><div class="ring"><svg width="34" height="34" viewBox="0 0 34 34" fill="none" stroke="#fff" stroke-width="1.6"><path d="M17 7a8 8 0 0 0-5 14v4h10v-4a8 8 0 0 0-5-14z"/><path d="M13 28h8M17 2v2M6 8l2 1M28 8l-2 1"/></svg></div><p>Sed ut perspiciatis unde omnis iste natus error sit voluptatem accusantium doloremque laudantium, totam rem aperiam</p></div>
</section>

<!-- APM strategy -->
<section class="slide apm">
  <svg class="bg" viewBox="0 0 985 553">
    <defs>
      <linearGradient id="robot" x1="0" y1="0" x2="1" y2="1">
        <stop offset="0" stop-color="#cfe4f6"/>
        <stop offset="0.6" stop-color="#8fbbe2"/>
        <stop offset="1" stop-color="#b9d6ef"/>
      </linearGradient>
    </defs>
    <polygon points="339,0 985,0 985,553" fill="url(#robot)" role="img" aria-label="Humanoid robot with a translucent blue shell"/>
    <polygon points="0,553 686,395 620,553" fill="var(--sky)"/>
  </svg>
  <h2 class="abs thin title">In which<br>cases does an APM<br>strategy apply?</h2>
  <ul class="checks">
    <li><svg width="14" height="14" viewBox="0 0 14 14"><circle cx="7" cy="7" r="7" fill="var(--title-blue)"/><path d="M4 7.2l2 2 4-4" stroke="#fff" stroke-width="1.6" fill="none"/></svg>Sed ut perspiciatis unde omnis iste natus error sit voluptatem accusantium doloremque laudantium, totam rem aperiam.</li>
    <li><svg width="14" height="14" viewBox="0 0 14 14"><circle cx="7" cy="7" r="7" fill="var(--title-blue)"/><path d="M4 7.2l2 2 4-4" stroke="#fff" stroke-width="1.6" fill="none"/></svg>Sed ut perspiciatis unde omnis iste natus error sit voluptatem accusantium.</li>
    <li><svg width="14" height="14" viewBox="0 0 14 14"><circle cx="7" cy="7" r="7" fill="var(--title-blue)"/><path d="M4 7.2l2 2 4-4" stroke="#fff" stroke-width="1.6" fill="none"/></svg>Doloremque laudantium, totam rem aperiam.</li>
    <li><svg width="14" height="14" viewBox="0 0 14 14"><circle cx="7" cy="7" r="7" fill="var(--title-blue)"/><path d="M4 7.2l2 2 4-4" stroke="#fff" stroke-width="1.6" fill="none"/></svg>Nemo enim ipsam voluptatem quia voluptas sit aspernatur aut.</li>
  </ul>
  <p class="abs note">Neque porro quisquam est, qui dolorem ipsum quia dolor sit amet, consectetur, adipisci velit, sed quia non numquam eius modi tempora incidunt ut labore et dolore magnam aliquam quaerat voluptatem.</p>
</section>

<!-- Hyper digitization -->
<section class="slide hyper">
  <svg class="bg" viewBox="0 0 985 553">
    <defs>
      <linearGradient id="engineer" x1="0" y1="0" x2="1" y2="1">
        <stop offset="0" stop-color="#8c99a8"/>
        <stop offset="0.5" stop-color="#c7cdd4"/>
        <stop offset="1" stop-color="#e4e8ec"/>
      </linearGradient>
    </defs>
    <polygon points="0,0 325,0 614,553 0,553" fill="url(#engineer)" role="img" aria-label="Engineer in a safety vest using a laptop beside a robotic arm"/>
    <polygon points="797,0 985,0 921,173" fill="var(--sky)"/>
    <polygon points="7,553 84,431 188,553" fill="var(--sky)"/>
  </svg>
  <h2 class="abs thin title">About<br>hyper digitization?</h2>
  <p class="para" style="left:492px;top:204px">Neque porro quisquam est, qui dolorem ipsum quia dolor sit amet, consectetur, adipisci velit, sed quia non numquam eius modi tempora incidunt ut labore et dolore magnam aliquam quaerat voluptatem.</p>
  <p class="para" style="left:512px;top:270px">Neque porro quisquam est, qui dolorem ipsum quia dolor sit amet, consectetur, adipisci velit, sed quia non numquam eius modi tempora incidunt ut labore et dolore magnam aliquam quaerat voluptatem.</p>
  <p class="para" style="left:540px;top:338px;width:430px">Neque porro quisquam est, qui dolorem ipsum quia dolor sit amet, consectetur, adipisci velit, sed quia non numquam eius modi tempora incidunt ut labore et dolore magnam aliquam quaerat voluptatem.</p>
  <p class="para" style="left:583px;top:407px;width:380px">Neque porro quisquam est, qui dolorem ipsum quia dolor sit amet, consectetur, adipisci velit, sed quia non numquam eius modi tempora incidunt ut labore et dolore magnam aliquam quaerat voluptatem.</p>
</section>

<!-- Contacts -->
<section class="slide contacts">
  <svg class="bg" viewBox="0 0 985 553">
    <defs>
      <radialGradient id="handBrain" cx="0.65" cy="0.45" r="0.6">
        <stop offset="0" stop-color="#6f9fd6"/>
        <stop offset="0.4" stop-color="#1c3a6e"/>
        <stop offset="1" stop-color="#060e22"/>
      </radialGradient>
    </defs>
    <polygon points="678,0 985,0 985,553 297,553" fill="url(#handBrain)" role="img" aria-label="Open hand holding a glowing digital brain"/>
    <polygon points="985,419 985,553 886,553" fill="var(--sky)"/>
  </svg>
  <h2 class="abs thin title">Contacts</h2>
  <div class="abs wordmark">Quelmoro</div>
  <div class="contact-row" style="top:250px"><span class="dot"><svg width="18" height="20" viewBox="0 0 18 20"><path d="M9 1a6.5 6.5 0 0 0-6.5 6.5C2.5 12 9 19 9 19s6.5-7 6.5-11.5A6.5 6.5 0 0 0 9 1z" fill="#fff"/><circle cx="9" cy="7.5" r="2.4" fill="var(--mid)"/></svg></span><span>Monterrey, NL Av. Rivera Solís<br># 218, Col. Alameda</span></div>
  <div class="contact-row" style="top:319px"><span class="dot"><svg width="18" height="18" viewBox="0 0 24 24"><path d="M6.6 10.8a15 15 0 0 0 6.6 6.6l2.2-2.2c.3-.3.7-.4 1-.2 1.1.4 2.3.6 3.6.6.6 0 1 .4 1 1V20c0 .6-.4 1-1 1A17 17 0 0 1 3 4c0-.6.4-1 1-1h3.5c.6 0 1 .4 1 1 0 1.3.2 2.5.6 3.6.1.3 0 .7-.2 1z" fill="#fff"/></svg></span><span>+52 81 5550 2718</span></div>
  <div class="contact-row" style="top:375px"><span class="dot"><svg width="20" height="16" viewBox="0 0 20 16"><rect x="1" y="1" width="18" height="14" rx="2" fill="#fff"/><path d="M2 3l8 6 8-6" stroke="var(--mid)" stroke-width="1.6" fill="none"/></svg></span><span>info@quelmoro-mx.com</span></div>
</section>

</body>
</html>
```